Building company with a modern and unique product looking for a business card to help us stand out

We currently have a logo but as our business has grown, we feel that our business card is not reflecting our modern and high quality product and help us stand out from the crowd. Our business is mainly in the construction of new homes using a unique method and materials that makes our homes fire proof, vermin and pest resistant and rated to the maximum cyclone category (category 5). We need a business card that helps us stand out as well as communicating professionalism, high quality and trustworthiness. I have attached our current logo with a black and white option, as well as our business card which is double sided. We would like to retain as much of the information that is currently on our business cards, but presented in a more sleek way. We do like our current colour palette ( white, black, yellow and grey) and have been looking primarily at business cards with a black background however we are open to other combinations of colour and layout as long as we stand out. Please feel free to tweak our logo to make it more suitable for a business card, we like the black option that we use but we have had trouble trying to get the white area to match the rest of the logo and blend effectively into a business card. Please do not hesitate to contact us with any questions as we really want this to be successful!

Target Market(s)

Large contracts including government and larger companies

Industry/Entity Type

Business

We will be providing this business card to potential clients including key government ministers and large funding companies, our business card should show that we are professional and reliable.

Requirements
Must have
• It must be easy to read and pleasing to the eye, It must contain as much of the information on the current business card and unless something really stands out, we will most likely pick a design that has all of the information included. It must include our logo of course and have some colour included.
Nice to have
• We are looking for a high end business card and would like to see designs that reflect this. We like the gloss/matte contrast, plastic cards with opaque/coloured areas and unique features not seen on everyday paper business cards. It would be nice to see a few different colour combinations, we are open to new ideas so please feel free to take some artistic licence.
Should not have
• Must not be too busy, difficult to read or be distracting from the information conveyed. Other than this please feel free to add your own touches and make it unique!

```html
<!DOCTYPE html>
<html lang="en">
<head>
<meta charset="UTF-8">
<title>Korvane Building Co. – Business Card</title>
<link rel="stylesheet" href="https://fonts.googleapis.com/css2?family=Open+Sans:wght@400;600;700&family=Roboto+Condensed:wght@400;500&family=Tinos&display=swap">
<style>
  :root{
    --backdrop:#b4b2b2;
    --card:#16171a;
    --gold:#d3a92e;
    --silver:#bfbfbf;
    --white:#ffffff;
    --ink:#1c1c1c;
    --muted:#e6e6e6;
  }
  *{margin:0;padding:0;box-sizing:border-box}
  html,body{width:1200px;height:1200px;overflow:hidden}
  body{background:var(--backdrop);position:relative;font-family:"Open Sans",sans-serif}

  .card{position:absolute;width:712px;height:419px;background:var(--card);border-radius:26px;overflow:hidden}
  .card--front{left:238px;top:118px}
  .card--back{left:231px;top:645px}

  /* Front */
  .brand{position:absolute;left:0;right:0;top:140px;text-align:center;color:var(--white);
    font-family:"Open Sans",sans-serif;font-weight:600;font-size:44px;letter-spacing:.5px;white-space:nowrap}
  .brand__mark{display:inline-block;width:16px;height:16px;background:var(--gold);margin-right:14px;vertical-align:middle;position:relative;top:-4px}
  .band{position:absolute;left:0;right:0;text-align:center;font-family:"Tinos",serif;font-size:19px;letter-spacing:.3px}
  .band--intro{top:312px;height:40px;line-height:40px;background:var(--white);color:var(--ink)}
  .band--features{top:352px;height:38px;line-height:38px;background:var(--gold);color:var(--ink)}

  /* Back */
  .accent-field{position:absolute;left:0;top:0;width:240px;height:419px;
    background:linear-gradient(90deg,rgba(211,169,46,.16) 0%,rgba(191,191,191,.08) 55%,rgba(22,23,26,0) 100%)}
  .contact{position:absolute;right:377px;top:110px;text-align:right;color:var(--white)}
  .contact__name{font-family:"Open Sans",sans-serif;font-weight:700;font-size:21px;color:var(--gold);line-height:30px}
  .contact__role{font-size:15px;color:var(--muted);line-height:22px}
  .contact__list{list-style:none;margin-top:33px;padding-right:23px;font-family:"Roboto Condensed",sans-serif;font-size:17px;line-height:25px}
  .contact__list li{display:flex;justify-content:flex-end;align-items:center;gap:10px}
  .contact__list svg{width:16px;height:16px;margin-right:-23px;margin-left:3px}
  .contact__abn{margin-top:10px;font-family:"Roboto Condensed",sans-serif;font-weight:500;font-size:17px;color:var(--gold);line-height:22px}
  .brand--back{left:370px;right:20px;top:192px;font-size:27px;line-height:36px}
  .brand--back .brand__mark{width:11px;height:11px;margin-right:9px;top:-3px}
</style>
</head>
<body>

<section class="card card--front" aria-label="Card front">
  <div class="brand"><span class="brand__mark"></span>Korvane Building Co.</div>
  <div class="band band--intro">Specialising in Homes that are:</div>
  <div class="band band--features">Fire Proof&nbsp; | &nbsp;Climate Proof&nbsp; | &nbsp;Cyclone Rated (Cat. 5)</div>
</section>

<section class="card card--back" aria-label="Card back">
  <div class="accent-field" role="img" aria-label="Gold and silver decorative accent area"></div>

  <div class="contact">
    <p class="contact__name">Daniel Whitford</p>
    <p class="contact__role">Managing Director</p>
    <ul class="contact__list">
      <li><span>0400 555 182</span>
        <svg viewBox="0 0 16 16" aria-label="Mobile"><path fill="#d3a92e" d="M2 6c0-2 2-3 6-3s6 1 6 3v1h-3V5.5H5V7H2zM4 8h8l1.5 5h-11z"/></svg></li>
      <li><span>(02) 5550 1934</span>
        <svg viewBox="0 0 16 16" aria-label="Office"><g fill="none" stroke="#d3a92e" stroke-width="1.4"><circle cx="8" cy="8" r="6.3"/><ellipse cx="8" cy="8" rx="2.8" ry="6.3"/><path d="M1.7 8h12.6M3 4.5h10M3 11.5h10"/></g></svg></li>
      <li><span>hello@korvanebuild.com</span>
        <svg viewBox="0 0 16 16" aria-label="Email"><rect x="1" y="3.5" width="14" height="9" fill="#d3a92e"/><path d="M1 3.5l7 5 7-5M1 12.5l5-4.5M15 12.5l-5-4.5" fill="none" stroke="#16171a" stroke-width="1.2"/></svg></li>
    </ul>
    <p class="contact__abn">ABN: 00 000 000 000</p>
  </div>

  <div class="brand brand--back"><span class="brand__mark"></span>Korvane Building Co.</div>
</section>

</body>
</html>
```